Refresh and update our Juice bottle label to a more vibrant and eye catching brand

We’ve had this label and included trademarked logo for the past 10 years. We do change the name of the juice ands its ingredients accordingly.
I want to up-date this round juice bottle label so it is more eye catching , trendy and clearly screams (healthy/juice/delicious/refreshing/beauty/youthful/high energy.
I have attached my trademarked logos as well as examples of a few labels. I also attached a few pictures of our juices with the current label which is a 2x4 inch front and back. I want you to see how colorful our juice is. I want the updated label to include out trademarked logo somehow but add in some color or graphics that speak to the message above in (). Open to adding color and even having a wrap around label instead of front and back=

Target Market(s)

Upscale women:men, age 20-65 40:30 ratio, health/ fitness/ body aware, anti aging/ high energy/ prevention of disease. Clientele is primarily caucasian.

Industry/Entity Type

Beverage, cold-pressed juice, wellness

Font styles to use
Sans Serif

Colors
59FF00
82FF00
B8FF75
E3FFCB
F4FFEA
EB3D1F
EC4F4E
F09395
F8D3D4
FCEDEE
E54698
E96AAD
F1A4CE
F9D9EA
FCEFF6
6B429C
8869AF
B7A5CE
E3DAEB
F3F0F8

Requirements
Must have
• My trademarked logo incorporated somehow. Bright/simple/modern/trendy style. I need to be able to change out the name of the juice and its ingredients and nutritional information. I want the label to say “100% Juice” basically this all needs to be on it: Name and Address. The name and address of your juicing business. ... Name of the Food. You should list the name of the food that is commonly used. ... What is the Amount of Juice inside of the bottle? ... % of juice declaration. ... Ingredients. ... Food Allergen (made in a facility with nuts). ... The Disclaimer. Must say “cold-pressed juice”
Nice to have
• Maybe a graphic image of a piece of fruit like a lemon with sliced cucumbers, I want vibrant colors added such as maybe use hot pink -outline or graphic on my Feel Rosy Bright? since the juice is pink. Or a bright yellow on my Zest Rising? Or a bright green on Lush Ace. Maybe some wording like “no added sugar or preservatives”, “gluten free”
Should not have
• No health guarantees

```html
<!DOCTYPE html>
<html lang="en">
<head>
<meta charset="utf-8">
<title>Lush Ace – Cold-Pressed Juice Label</title>
<link rel="stylesheet" href="https://fonts.googleapis.com/css2?family=Montserrat:wght@400;500;600;700;800&display=swap">
<style>
  :root {
    --canvas: #ffffff;
    --label-bg: #ffffff;
    --forest: #0e7d3e;
    --mint: #7fc08f;
    --lime-soft: #c2dc6b;
    --leaf: #2e8b3d;
    --ink: #3a3a3a;
    --ink-soft: #4a4a4a;
    --art-lemon: #f2c21b;
    --art-cucumber: #6fae3c;
  }
  html, body {
    margin: 0;
    padding: 0;
    width: 1200px;
    height: 2800px;
    overflow: hidden;
    background: var(--canvas);
  }
  .label {
    position: absolute;
    left: 50px;
    top: 654px;
    width: 1100px;
    height: 1492px;
    display: block;
    background: var(--label-bg);
  }
  .label text { font-family: "Montserrat", sans-serif; }
  .brand-name { font-weight: 800; fill: var(--leaf); font-size: 46px; }
  .arch-line { fill: none; stroke: var(--forest); stroke-width: 2.2; }
  .dot-rule { stroke: var(--ink); stroke-width: 4; stroke-linecap: round; stroke-dasharray: 0 10; }
  .dot-rule--short { stroke: var(--art-cucumber); }
  .arch-caption { font-weight: 600; font-size: 28px; fill: var(--ink); letter-spacing: 2px; }
  .freshness-note { font-weight: 400; font-size: 24px; fill: var(--ink); letter-spacing: 2px; }
  .juice-name { font-weight: 700; font-size: 96px; fill: var(--ink); }
  .ingredient { font-weight: 600; font-size: 22px; fill: var(--forest); letter-spacing: 2.5px; }
  .process-line { font-weight: 600; font-size: 34px; fill: var(--ink); }
  .net-weight { font-weight: 400; font-size: 22px; fill: var(--ink-soft); }
  .doodle { fill: #ffffff; opacity: 0.22; }
  .doodle--dark { fill: var(--forest); opacity: 0.18; }
</style>
</head>
<body>
<svg class="label" viewBox="0 0 785 1065" xmlns="http://www.w3.org/2000/svg">
  <defs>
    <path id="arch-top-path" d="M240,470 V417 A152,152 0 0 1 544,417 V470"/>
    <path id="arch-bottom-path" d="M220,606 V730 A172,172 0 0 0 564,730 V606"/>
    <radialGradient id="produce-tone" cx="50%" cy="45%" r="60%">
      <stop offset="0%" stop-color="#f5d94a"/>
      <stop offset="100%" stop-color="#5d9f35"/>
    </radialGradient>
  </defs>

  <!-- background shapes -->
  <g class="blobs">
    <path fill="var(--forest)" d="M0,0 H230 C180,40 130,70 120,120 C110,170 60,190 0,195 Z"/>
    <path fill="var(--lime-soft)" d="M0,200 C60,185 120,150 165,170 C200,190 170,240 140,260 C120,280 185,300 175,340 C160,370 90,350 60,340 C30,330 10,330 0,335 Z"/>
    <path fill="var(--mint)" d="M600,0 H785 V430 C740,420 700,390 670,350 C630,300 600,240 640,180 C670,130 620,60 600,0 Z"/>
    <path fill="var(--forest)" d="M785,130 C730,120 660,150 650,210 C640,270 680,330 740,340 C760,342 775,335 785,330 Z"/>
    <path fill="var(--mint)" d="M0,700 C50,690 90,720 100,780 C110,840 150,900 200,960 C210,1000 190,1040 195,1065 H0 Z"/>
    <path fill="var(--lime-soft)" d="M40,790 C90,770 150,790 175,840 C200,900 190,960 140,980 C90,995 30,975 20,920 C10,870 5,810 40,790 Z"/>
    <path fill="var(--forest)" d="M785,660 V1065 H570 C600,1010 580,960 600,900 C620,830 660,760 720,710 C745,690 765,672 785,660 Z"/>
    <path fill="var(--lime-soft)" d="M620,940 C660,930 700,960 720,1000 C730,1030 725,1050 720,1065 H575 C590,1020 595,960 620,940 Z"/>
  </g>

  <!-- line-art produce placeholders -->
  <g role="img" aria-label="Line drawing of a lemon slice">
    <circle class="doodle" cx="40" cy="70" r="55"/>
  </g>
  <g role="img" aria-label="Line drawing of parsley leaves">
    <circle class="doodle--dark" cx="70" cy="265" r="45"/>
  </g>
  <g role="img" aria-label="Line drawing of a ginger root">
    <ellipse class="doodle--dark" cx="635" cy="40" rx="70" ry="38"/>
  </g>
  <g role="img" aria-label="Line drawing of parsley leaves">
    <circle class="doodle" cx="700" cy="240" r="55"/>
  </g>
  <g role="img" aria-label="Line drawing of a lemon slice">
    <circle class="doodle--dark" cx="50" cy="585" r="52"/>
  </g>
  <g role="img" aria-label="Line drawing of a lime slice">
    <circle class="doodle--dark" cx="730" cy="535" r="55"/>
  </g>
  <g role="img" aria-label="Line drawing of a ginger root">
    <ellipse class="doodle" cx="115" cy="850" rx="60" ry="55"/>
  </g>
  <g role="img" aria-label="Line drawing of parsley sprigs">
    <ellipse class="doodle" cx="690" cy="830" rx="75" ry="80"/>
  </g>

  <!-- brand -->
  <g class="brand">
    <circle cx="235" cy="130" r="26" fill="var(--leaf)"/>
    <text class="brand-name" x="278" y="122">Verdant</text>
    <text class="brand-name" x="278" y="172">Sip Co.</text>
  </g>

  <!-- upper arch -->
  <path class="arch-line" d="M195,465 V417 A197,197 0 0 1 589,417 V465"/>
  <path class="arch-line" d="M272,465 V410 A120,120 0 0 1 512,410 V465"/>
  <text class="arch-caption"><textPath href="#arch-top-path" startOffset="4" textLength="575" lengthAdjust="spacing">100% VEGETABLE &amp; FRUIT JUICE</textPath></text>
  <g role="img" aria-label="Illustration of cucumber pieces and a lemon wedge">
    <ellipse cx="392" cy="385" rx="86" ry="64" fill="url(#produce-tone)"/>
  </g>

  <!-- juice name -->
  <line class="dot-rule" x1="197" y1="482" x2="589" y2="482"/>
  <text class="juice-name" x="392" y="572" text-anchor="middle" textLength="540" lengthAdjust="spacingAndGlyphs">LUSH ACE</text>
  <line class="dot-rule" x1="197" y1="594" x2="589" y2="594"/>

  <!-- lower arch -->
  <path class="arch-line" d="M195,606 V730 A197,197 0 0 0 589,730 V606"/>
  <path class="arch-line" d="M272,606 V710 A120,120 0 0 0 512,710 V606"/>
  <text class="freshness-note"><textPath href="#arch-bottom-path" startOffset="6" textLength="780" lengthAdjust="spacing">BEST IF USED WITHIN 5 DAYS OF PURCHASE</textPath></text>

  <g class="ingredients" text-anchor="middle">
    <text class="ingredient" x="392" y="634">SPINACH</text>
    <text class="ingredient" x="392" y="662">CUCUMBER</text>
    <text class="ingredient" x="392" y="690">CELERY</text>
    <text class="ingredient" x="392" y="718">PARSLEY</text>
    <text class="ingredient" x="392" y="746">PINEAPPLE</text>
    <text class="ingredient" x="392" y="774">LEMON</text>
    <text class="ingredient" x="392" y="802">GINGER</text>
  </g>

  <!-- footer -->
  <text class="process-line" x="392" y="980" text-anchor="middle">COLD-PRESSED JUICE</text>
  <line class="dot-rule dot-rule--short" x1="305" y1="1002" x2="480" y2="1002"/>
  <text class="net-weight" x="392" y="1038" text-anchor="middle">Net Wt. 12oz (354mL)</text>
</svg>
</body>
</html>
```